One page responsive Wordpress Website

I am looking to design and code for 1-page Wordpress responsive website (desktop/mobile/tablet). Pls see attached file. Job scope includes Wordpress design and coding of the actual Live website
Target Market(s)
Small medium business
Industry/Entity Type
Telecommunications
Font styles to use
Sans Serif
Colors
ffffff
85cae6
63bae0
33a6d7
cedeed
3277b5
Requirements
Must have
- One page only, Wordpress, Responsive layout in desktop, mobile, tablet

```html
<!DOCTYPE html>
<html lang="en">
<head>
<meta charset="utf-8">
<title>Veltora IP Phone</title>
<link href="https://fonts.googleapis.com/css2?family=Poppins:wght@300;400;500;600;700&display=swap" rel="stylesheet">
<style>
:root{
  --white:#ffffff;
  --sky:#85cae6;
  --sky-mid:#63bae0;
  --azure:#33a6d7;
  --mist:#cedeed;
  --blue:#3277b5;
  --navy:#0f2f6b;
  --footer:#0f4f9e;
  --text:#5a5a5a;
  --ring:#cde5ef;
  --ring-fill:#eef6fa;
  --sand:#f3f1ee;
}
*{margin:0;padding:0;box-sizing:border-box}
html,body{width:1200px;height:2734px;overflow:hidden}
body{position:relative;background:var(--white);font-family:'Poppins',sans-serif;color:var(--text)}
.abs{position:absolute}

.site-header{left:0;top:0;width:1200px;height:86px;background:linear-gradient(90deg,#e6f2f7,#cfe4ee 50%,#e6f2f7);z-index:3}
.brand{font-weight:700;color:var(--azure);font-size:48px;letter-spacing:-1px;line-height:1}
.site-header .brand{left:144px;top:18px}
.nav-btn{top:26px;height:36px;border-radius:18px;background:var(--azure);color:var(--white);font-size:18px;display:flex;align-items:center;justify-content:center}

.hero{left:0;top:86px;width:1200px;height:600px}
.hero-title{left:144px;top:400px;color:var(--white);font-size:52px;font-weight:400;line-height:64px}
.hero-title b{font-weight:700}

.intro-title{left:0;top:715px;width:1200px;text-align:center;font-size:80px;font-weight:600;color:var(--blue);line-height:1}
.intro-text{left:0;top:826px;width:1200px;text-align:center;font-size:22px;font-weight:300;color:var(--blue);line-height:32px}

.product{width:290px;text-align:center}
.product-ring{left:0;top:0;width:290px;height:290px;border-radius:50%;background:var(--ring-fill);border:21px solid var(--ring)}
.product-maker{left:0;top:42px;width:290px;font-size:13px;font-weight:500;color:#222}
.product-model{left:0;top:60px;width:290px;font-size:24px;font-weight:600;color:var(--azure)}
.product-photo{left:80px;top:100px;width:130px;height:140px;border-radius:8px;background:linear-gradient(160deg,#4b5968,#2b3642)}
.sheet-btn{left:9px;top:302px;width:272px;height:48px;border-radius:24px;background:var(--azure);color:var(--white);font-size:19px;display:flex;align-items:center;justify-content:center}
.feature-row{top:1330px;display:flex;gap:15px}
.feature{width:30px;height:30px;border-radius:50%;background:var(--mist);color:var(--blue);font-size:9px;font-weight:700;display:flex;align-items:center;justify-content:center;line-height:1}

.about-title{left:144px;top:1493px;font-size:50px;font-weight:500;color:var(--navy)}
.about-text{left:144px;top:1568px;width:430px;font-size:17px;line-height:32px;font-weight:300}
.about-art{left:615px;top:1465px}

.contact{left:0;top:2001px;width:1200px;height:527px;background:var(--sand)}
.contact-photo{left:0;top:0;width:625px;height:527px;background:linear-gradient(120deg,#d9d2c8,#b7a998 45%,#3e3a3c 75%,#efece8)}
.contact-title{left:627px;top:2030px;font-size:50px;font-weight:500;color:var(--navy)}
.contact-lead{left:627px;top:2098px;width:420px;font-size:22px;line-height:32px;color:#1a1a1a}
.contact-text{left:627px;top:2172px;width:440px;font-size:17px;line-height:29px;font-weight:300}
.field{border:1px solid #bfbfbf;background:var(--white);font-size:12px;color:#888;padding:12px 14px}
.submit{left:630px;top:2439px;width:111px;height:46px;border-radius:23px;background:var(--azure);color:var(--white);font-size:19px;display:flex;align-items:center;justify-content:center}

.site-footer{left:0;top:2528px;width:1200px;height:206px;background:radial-gradient(circle at 30% 40%,#1a5db0,var(--footer) 70%)}
.site-footer .brand{left:144px;top:28px;font-size:40px;color:var(--white)}
.footer-small{color:var(--white);font-size:12px;font-weight:300}
.footer-head{left:778px;top:30px;font-size:22px;font-weight:600;color:var(--white)}
.footer-item{left:778px;display:flex;align-items:center;gap:14px}
.footer-item svg{width:12px;height:12px;fill:var(--white)}
</style>
</head>
<body>

<header class="abs site-header">
  <div class="abs brand">Veltora</div>
  <a class="abs nav-btn" style="left:790px;width:119px">About Us</a>
  <a class="abs nav-btn" style="left:919px;width:136px">Contact Us</a>
</header>

<section class="abs hero">
  <svg width="1200" height="600" viewBox="0 0 1200 600" role="img" aria-label="Businessman in a suit smiling while talking on a desk phone in a bright office">
    <defs>
      <linearGradient id="heroFill" x1="0" y1="0" x2="1" y2="1">
        <stop offset="0" stop-color="#3a4a58"/>
        <stop offset="0.45" stop-color="#6c7f8f"/>
        <stop offset="0.75" stop-color="#23304a"/>
        <stop offset="1" stop-color="#aab9c4"/>
      </linearGradient>
    </defs>
    <rect width="1200" height="600" fill="url(#heroFill)"/>
    <path d="M0 530 Q600 680 1200 530 L1200 600 L0 600 Z" fill="#ffffff"/>
  </svg>
  <h1 class="abs hero-title" style="top:314px">Enterprise<br><b>HD</b> IP Phone</h1>
</section>

<h2 class="abs intro-title">Veltora IP Phone</h2>
<p class="abs intro-text">The most affordable IP Phone, with highest compatibility to<br>every IP-PBX system. Sleek designed and user-friendly proven.</p>

<div class="abs product" style="left:145px;top:967px">
  <div class="abs product-ring"></div>
  <div class="abs product-maker">Veltora</div>
  <div class="abs product-model">VX310</div>
  <div class="abs product-photo" role="img" aria-label="Dark grey desk IP phone with colour screen and keypad"></div>
  <a class="abs sheet-btn">Download datasheet (EN)</a>
</div>
<div class="abs product" style="left:455px;top:967px">
  <div class="abs product-ring"></div>
  <div class="abs product-maker">Veltora</div>
  <div class="abs product-model">VX320</div>
  <div class="abs product-photo" role="img" aria-label="Dark grey desk IP phone with colour screen and navigation keys"></div>
  <a class="abs sheet-btn">Download datasheet (EN)</a>
</div>
<div class="abs product" style="left:765px;top:967px">
  <div class="abs product-ring"></div>
  <div class="abs product-maker">Veltora</div>
  <div class="abs product-model">VX40</div>
  <div class="abs product-photo" style="left:105px;width:80px" role="img" aria-label="Expansion module with tall display of contact keys"></div>
  <a class="abs sheet-btn">Download datasheet (EN)</a>
</div>

<div class="abs feature-row" style="left:207px">
  <span class="feature">HD</span><span class="feature">LAN</span><span class="feature">BK</span><span class="feature">GRP</span>
</div>
<div class="abs feature-row" style="left:472px">
  <span class="feature">100M</span><span class="feature">2.8"</span><span class="feature">HD</span><span class="feature">LAN</span><span class="feature">BK</span><span class="feature">GRP</span>
</div>

<h2 class="abs about-title">About Us</h2>
<p class="abs about-text">Veltora IP Phones is designed with pixel colour LCD with backlight LED, built-in Gigabit Ethernet with up to 28 various features. Equipped with Power over Ethernet (PoE) support, and high definition (HD) sound quality with a rich visual experience. Designed with a fresh appearance, it supports flexible and secured provisioning, deliver modern elegant appearance, superb sound quality and a rich set of IP/SIP telephony features.</p>

<svg class="abs about-art" width="450" height="410" viewBox="0 0 450 410">
  <defs>
    <linearGradient id="aboutFill" x1="0" y1="0" x2="1" y2="1">
      <stop offset="0" stop-color="#3c3a3b"/>
      <stop offset="0.5" stop-color="#c9c2bb"/>
      <stop offset="1" stop-color="#f1efec"/>
    </linearGradient>
  </defs>
  <path d="M300 20 Q350 -10 390 30 L160 250 Q60 300 10 240 Q-10 200 40 170 Z" fill="#cedeed"/>
  <path d="M410 30 Q440 20 440 60 L360 330 Q340 410 270 400 L90 260 Q20 210 60 170 L360 40 Z" fill="url(#aboutFill)" role="img" aria-label="Smiling woman in a white top talking on a desk phone"/>
</svg>

<section class="abs contact">
  <div class="abs contact-photo" role="img" aria-label="Young man in a dark jacket talking on a corded phone"></div>
</section>
<h2 class="abs contact-title">Contact Us Now</h2>
<p class="abs contact-lead">Speak to us or send us an enquiry for free consultation.</p>
<p class="abs contact-text">Our team would love to share more about Veltora IP Phones. We are expecting your calls and emails. Drop us an enquiry form at your fingertips!</p>
<div class="abs field" style="left:630px;top:2278px;width:207px;height:40px">Name</div>
<div class="abs field" style="left:847px;top:2278px;width:208px;height:40px">Email Address</div>
<div class="abs field" style="left:630px;top:2329px;width:425px;height:95px">Message</div>
<a class="abs submit">Submit</a>

<footer class="abs site-footer">
  <div class="abs brand">Veltora</div>
  <p class="abs footer-small" style="left:144px;top:100px">Copyright © 2021 Company Name. All rights reserved.</p>
  <p class="abs footer-small" style="left:144px;top:127px">Home &nbsp;•&nbsp; About Us &nbsp;•&nbsp; Contact Us</p>
  <h3 class="abs footer-head">Contact us</h3>
  <div class="abs footer-item footer-small" style="top:70px">
    <svg viewBox="0 0 12 12"><path d="M6 0a4 4 0 0 0-4 4c0 3 4 8 4 8s4-5 4-8a4 4 0 0 0-4-4zm0 5.5A1.5 1.5 0 1 1 6 2.5a1.5 1.5 0 0 1 0 3z"/></svg>
    <span>48 Harbour Lane, #05-12, Singapore 100000</span>
  </div>
  <div class="abs footer-item footer-small" style="top:97px">
    <svg viewBox="0 0 12 12"><path d="M2.5 0 4.5 2.6 3.4 4a7 7 0 0 0 4.6 4.6L9.4 7.5 12 9.5 10.8 11.6C5 12 0 7 .4 1.2z"/></svg>
    <span>6000-1234</span>
  </div>
  <div class="abs footer-item footer-small" style="top:124px">
    <svg viewBox="0 0 12 12"><path d="M0 2h12v8H0zM0 2l6 4 6-4v1.4L6 7.4 0 3.4z"/></svg>
    <span>enquiry@northwire.example</span>
  </div>
  <div class="abs footer-item footer-small" style="top:151px">
    <svg viewBox="0 0 12 12"><circle cx="6" cy="6" r="5"/></svg>
    <span>Northwire Business Systems Pte Ltd</span>
  </div>
</footer>

</body>
</html>
```